New therapy private practice needs a 2 sided postcard announcing location and services

We need a postcard sized card that is TWO SIDED and shares our new location and services offered. (new location is 3840. W. 58th #2200 in Tulsa, OK 74129) Name of the therapy business is "Calm Harbor Counseling". Services offered include individual, marriage, family and group counseling. My phone number to place on the card is (918) 555-0148 and someone can call to schedule a free 20 minute consultation at that number.

These cards will also be mailed in an enclosed envelope or placed in welcome baskets as a marketing tool with possible referral sources like churches, doctors, and lawyers. (That means there does not have to be a space for an address or stamp to mail to. Full use of both sides of the card is important) We would like to see designs that use softer colors such as blue, purples, or greens. The final design should communicate a feeling of peace and hope and a sense of freshness and approachability. Incorporating a tag line such as..... "where you'll find hope!" would be good. My website is www.calmharborcare.example and extra info about my practice is on there. It is important my credentials are listed on the postcard. Dana Ruth Pell, LPC-S, LMFT

I am not looking for a bunch of "box looking pictures". The pictures I am uploading are for ideas, although my logo and picture should be used. I like the type of picture I have on my homepage of my website with the quote "Let your hopes, not your fears shape your future"

Target Market(s)

Primarily women and couples looking for counseling for relationships, anxiety, depression, or life transitions.

Font styles to use
Serif
Script

Colors
3276b5
85acd3
86cfc6
33b8a4
cadf82
876aae
9bcb3c

Requirements
Must have
• My picture, address, website, and phone number as well as my logo.
• Address is: 3840 W. 58th Street #2200 Tulsa, OK 74129
• Web: www.calmharborcare.example
• Email: dana@calmharborcare.example
• Phone: (918) 555-0148
• "Hope anchors the soul" - Heb. 6:19
• On my website, I have a 2 minute video of myself. This may be helpful to watch in getting a "feel" for my counseling practice.
• Services Provided: ANXIETY | DEPRESSION | LIFE TRANSITIONS | MARRIAGE COUNSELING | SEPARATION AND DIVORCE | WOMEN’S ISSUES | ADDICTIONS AND INFIDELITY | PARENT/CHILD RELATIONSHIPS | FAMILY CONFLICT | TRAUMA/GRIEF AND LOSS
Nice to have
• A combination of print and script would be nice. A feeling of tranquility and hope
• I would like to have the statement at the bottom of the card.... " It is my desire for you to discover that no matter the situation you are currently going through….. there’s hope!"
• It would also be nice to have a small area that says: Dana is a graduate of Western Lakeview College and has been in private practice for 11 years. She is a regular monthly co-host on the Meadow Broadcast Group at 88.3 FM
Should not have
• Heavy bold or abrasive feel

```html
<!DOCTYPE html>
<html lang="en">
<head>
<meta charset="utf-8">
<title>Calm Harbor Counseling – Postcard</title>
<link rel="stylesheet" href="https://fonts.googleapis.com/css2?family=Open+Sans:wght@400;600;700&family=Kaushan+Script&family=Parisienne&display=swap">
<style>
  :root{
    --purple:#876aae;
    --purple-deep:#7a5ea6;
    --blue:#3276b5;
    --teal:#33b8a4;
    --green:#5f9a2c;
    --ink:#1c1c1c;
    --white:#ffffff;
    --backdrop:#e4e5e8;
  }
  *{box-sizing:border-box;margin:0;padding:0}
  html,body{width:1200px;height:900px;overflow:hidden}
  body{background:var(--backdrop);font-family:"Open Sans",Arial,sans-serif;position:relative}
  .card{position:absolute;width:560px;height:386px;background:var(--white);overflow:hidden;box-shadow:0 10px 28px rgba(0,0,0,.22)}
  .card svg.art{position:absolute;inset:0;width:100%;height:100%}
  .card--front{left:30px;top:40px}
  .card--back{left:610px;top:474px}

  /* front */
  .brand{position:absolute;left:34px;top:52px;display:flex;align-items:center;gap:10px}
  .brand__dot{width:38px;height:38px;border-radius:50%;background:var(--green)}
  .brand__name{font-weight:600;font-size:19px;line-height:1.1;color:var(--green);width:130px}
  .quote{position:absolute;right:34px;top:178px;text-align:right;color:var(--white);text-shadow:0 1px 4px rgba(0,0,0,.45)}
  .quote__lead{font-weight:700;font-size:28px;line-height:1.15}
  .quote__line{font-weight:400;font-size:28px;line-height:1.15}
  .quote__source{font-size:12px;letter-spacing:.5px;margin-top:6px}
  .front-web{position:absolute;left:0;right:0;bottom:16px;text-align:center;font-weight:700;font-size:20px;color:var(--ink)}

  /* back */
  .services{position:absolute;left:26px;top:44px;color:var(--white)}
  .services__title{font-family:"Kaushan Script",cursive;font-size:24px;line-height:1;border-bottom:1.5px solid rgba(255,255,255,.8);padding-bottom:3px;display:inline-block}
  .service-list{list-style:none;font-size:11.5px;line-height:1.45}
  .service-list li{display:flex;align-items:center;gap:6px}
  .service-list--a{position:absolute;left:36px;top:92px}
  .service-list--b{position:absolute;left:210px;top:52px}
  .tick{width:10px;height:10px;flex:none}
  .credentials{position:absolute;left:36px;top:176px;color:var(--white);font-size:11px;line-height:1.35}
  .credentials strong{font-weight:700;font-size:12px}
  .contact{position:absolute;left:36px;top:222px;list-style:none;color:var(--white);font-size:10.5px;line-height:1.4}
  .contact li{display:flex;align-items:flex-start;gap:7px}
  .contact svg{width:10px;height:10px;flex:none;margin-top:3px}
  .radio-note{position:absolute;left:0;top:290px;width:400px;height:26px;padding-left:36px;display:flex;align-items:center;color:var(--white);font-weight:600;font-size:10.5px}
  .closing{position:absolute;left:30px;right:24px;top:318px;color:var(--purple)}
  .closing__text{font-family:"Parisienne",cursive;font-size:19px;line-height:1.05}
  .closing__text .mark{font-family:Georgia,serif;font-weight:700;font-size:22px}
  .closing__verse{text-align:right;font-weight:600;font-size:12px;margin-top:2px;padding-right:60px}
</style>
</head>
<body>

<section class="card card--front" aria-label="Postcard front">
  <svg class="art" viewBox="0 0 560 386" preserveAspectRatio="none">
    <defs>
      <radialGradient id="sunset" cx="0.8" cy="0.05" r="1">
        <stop offset="0" stop-color="#efe3c4"/>
        <stop offset="0.3" stop-color="#a79a7c"/>
        <stop offset="0.65" stop-color="#4d4431"/>
        <stop offset="1" stop-color="#241d14"/>
      </radialGradient>
    </defs>
    <path role="img" aria-label="Photo: a person sitting on a rock looking over a misty mountain forest at sunrise" d="M0,170 C170,155 360,110 495,0 L560,0 L560,330 L0,330 Z" fill="url(#sunset)"/>
    <path d="M0,128 C180,118 370,70 455,0 L495,0 C360,110 170,155 0,170 Z" fill="var(--purple)"/>
    <path d="M150,116 C290,96 400,48 462,0" fill="none" stroke="var(--blue)" stroke-width="4"/>
  </svg>
  <div class="brand">
    <span class="brand__dot"></span>
    <span class="brand__name">Calm Harbor Counseling</span>
  </div>
  <div class="quote">
    <p class="quote__lead">Let your Hopes,</p>
    <p class="quote__line">not your hurts,</p>
    <p class="quote__line">shape your future.</p>
    <p class="quote__source">-MARTIN J. ELLERY</p>
  </div>
  <p class="front-web">www.calmharborcare.example</p>
</section>

<section class="card card--back" aria-label="Postcard back">
  <svg class="art" viewBox="0 0 560 386" preserveAspectRatio="none">
    <defs>
      <linearGradient id="portrait" x1="0" y1="0" x2="0" y2="1">
        <stop offset="0" stop-color="#e9e4de"/>
        <stop offset="0.5" stop-color="#c9ad8a"/>
        <stop offset="1" stop-color="#3a2a3a"/>
      </linearGradient>
    </defs>
    <path d="M0,36 L425,36 C398,90 392,230 402,290 L0,290 Z" fill="var(--purple)"/>
    <rect x="0" y="290" width="400" height="26" fill="var(--teal)"/>
    <path role="img" aria-label="Portrait of the counselor, smiling, in a dark cardigan" d="M440,16 L560,16 L560,316 L398,316 C382,240 382,80 440,16 Z" fill="url(#portrait)"/>
    <path d="M440,16 C410,50 396,100 394,150" fill="none" stroke="var(--blue)" stroke-width="3"/>
  </svg>

  <div class="services"><h2 class="services__title">Services provided:</h2></div>

  <ul class="service-list service-list--a">
    <li><svg class="tick" viewBox="0 0 10 10"><circle cx="5" cy="5" r="4.2" fill="none" stroke="#fff" stroke-width="1"/><path d="M3,5 L4.5,6.5 L7,3.6" fill="none" stroke="#fff" stroke-width="1"/></svg>Anxiety</li>
    <li><svg class="tick" viewBox="0 0 10 10"><circle cx="5" cy="5" r="4.2" fill="none" stroke="#fff" stroke-width="1"/><path d="M3,5 L4.5,6.5 L7,3.6" fill="none" stroke="#fff" stroke-width="1"/></svg>Depression</li>
    <li><svg class="tick" viewBox="0 0 10 10"><circle cx="5" cy="5" r="4.2" fill="none" stroke="#fff" stroke-width="1"/><path d="M3,5 L4.5,6.5 L7,3.6" fill="none" stroke="#fff" stroke-width="1"/></svg>Life transitions</li>
    <li><svg class="tick" viewBox="0 0 10 10"><circle cx="5" cy="5" r="4.2" fill="none" stroke="#fff" stroke-width="1"/><path d="M3,5 L4.5,6.5 L7,3.6" fill="none" stroke="#fff" stroke-width="1"/></svg>Marriage counseling</li>
    <li><svg class="tick" viewBox="0 0 10 10"><circle cx="5" cy="5" r="4.2" fill="none" stroke="#fff" stroke-width="1"/><path d="M3,5 L4.5,6.5 L7,3.6" fill="none" stroke="#fff" stroke-width="1"/></svg>Separation and divorce</li>
  </ul>

  <ul class="service-list service-list--b">
    <li><svg class="tick" viewBox="0 0 10 10"><circle cx="5" cy="5" r="4.2" fill="none" stroke="#fff" stroke-width="1"/><path d="M3,5 L4.5,6.5 L7,3.6" fill="none" stroke="#fff" stroke-width="1"/></svg>Women’s issues</li>
    <li><svg class="tick" viewBox="0 0 10 10"><circle cx="5" cy="5" r="4.2" fill="none" stroke="#fff" stroke-width="1"/><path d="M3,5 L4.5,6.5 L7,3.6" fill="none" stroke="#fff" stroke-width="1"/></svg>Addictions and infidelity</li>
    <li><svg class="tick" viewBox="0 0 10 10"><circle cx="5" cy="5" r="4.2" fill="none" stroke="#fff" stroke-width="1"/><path d="M3,5 L4.5,6.5 L7,3.6" fill="none" stroke="#fff" stroke-width="1"/></svg>Parent/child relationships</li>
    <li><svg class="tick" viewBox="0 0 10 10"><circle cx="5" cy="5" r="4.2" fill="none" stroke="#fff" stroke-width="1"/><path d="M3,5 L4.5,6.5 L7,3.6" fill="none" stroke="#fff" stroke-width="1"/></svg>Family conflict</li>
    <li><svg class="tick" viewBox="0 0 10 10"><circle cx="5" cy="5" r="4.2" fill="none" stroke="#fff" stroke-width="1"/><path d="M3,5 L4.5,6.5 L7,3.6" fill="none" stroke="#fff" stroke-width="1"/></svg>Trauma/grief and loss</li>
  </ul>

  <div class="credentials">
    <p><strong>Dana Pell, LPC, LMFT</strong></p>
    <p>Licensed Professional Counselor</p>
    <p>Licensed Marriage and Family Therapist</p>
  </div>

  <ul class="contact">
    <li><svg viewBox="0 0 10 10"><path d="M5,0.5 C2.8,0.5 1.5,2.1 1.5,3.8 C1.5,6.3 5,9.5 5,9.5 C5,9.5 8.5,6.3 8.5,3.8 C8.5,2.1 7.2,0.5 5,0.5 Z" fill="#fff"/><circle cx="5" cy="3.8" r="1.3" fill="var(--purple)"/></svg><span>3840 W. 58th Street #2200 Tulsa, OK 74129</span></li>
    <li><svg viewBox="0 0 10 10"><circle cx="5" cy="5" r="4.2" fill="none" stroke="#fff" stroke-width="1"/><ellipse cx="5" cy="5" rx="1.8" ry="4.2" fill="none" stroke="#fff" stroke-width="0.8"/><path d="M0.8,5 H9.2" stroke="#fff" stroke-width="0.8"/></svg><span>www.calmharborcare.example</span></li>
    <li><svg viewBox="0 0 10 10"><rect x="0.5" y="2" width="9" height="6.5" fill="#fff"/><path d="M0.5,2 L5,5.8 L9.5,2" fill="none" stroke="var(--purple)" stroke-width="0.9"/></svg><span>dana@calmharborcare.example</span></li>
    <li><svg viewBox="0 0 10 10"><circle cx="5" cy="5" r="4.5" fill="#fff"/><path d="M3.4,2.8 L4.3,4 L3.9,4.6 C4.3,5.4 4.8,5.9 5.5,6.2 L6.1,5.8 L7.2,6.7 L6.6,7.5 C4.8,7.3 2.9,5.4 2.7,3.4 Z" fill="var(--purple)"/></svg><span>(918) 555-0148</span></li>
  </ul>

  <p class="radio-note">Dana can be heard monthly on the Meadow Broadcast Group at 88.3 FM</p>

  <div class="closing">
    <p class="closing__text"><span class="mark">“</span> It is my desire for you to discover that no matter the situation you are currently going through ..there’s hope! <span class="mark">”</span></p>
    <p class="closing__verse">Hope anchors the soul - Hebrews 6:19</p>
  </div>
</section>

</body>
</html>
```